Need business cards for our e-assessment business

We need professional looking business cards for our e-assessment business based in Europe. Our company is called Velmora.

You can just use sample name and addresses.

The colours we use are:

#70abe4 (blue)
#FF6600 (orange)

The back side should say: Assessment, simplified

This is the print-shop we are using. Please look at the link for info about formats: http://nl.pribbly-print.com/help/faq/using-my-own-artwork.html

Target Market(s)

Target market is education and large corporations

Industry/Entity Type

Business

```html
<!DOCTYPE html>
<html lang="en">
<head>
<meta charset="utf-8">
<title>Velmora business cards</title>
<link href="https://fonts.googleapis.com/css2?family=Open+Sans:wght@300;400&family=Arimo:wght@400;700&display=swap" rel="stylesheet">
<style>
  :root {
    --stage: #141414;
    --navy: #28303a;
    --paper: #ffffff;
    --orange: #ff6600;
    --peach: #fbe6d8;
    --ink: #4a4a4a;
    --ink-soft: #6e6e6e;
    --light: #e9ecef;
  }
  * { margin: 0; padding: 0; box-sizing: border-box; }
  html, body { width: 1200px; height: 871px; overflow: hidden; background: var(--stage); }
  .stage { position: relative; width: 1200px; height: 871px; }

  .card {
    position: absolute;
    width: 540px;
    height: 350px;
    border-radius: 18px;
    overflow: hidden;
  }

  /* back side */
  .card-back { left: 70px; top: 110px; background: var(--navy); }
  .card-back .brand { position: absolute; left: 128px; top: 120px; display: flex; align-items: center; gap: 22px; }
  .card-back .brand-dot { width: 76px; height: 76px; border-radius: 50%; background: var(--orange); }
  .card-back .brand-name {
    font-family: "Open Sans", sans-serif; font-weight: 300; font-size: 74px;
    color: var(--light); line-height: 1; letter-spacing: 1px;
  }
  .card-back .tagline {
    position: absolute; left: 228px; top: 206px;
    font-family: "Arimo", sans-serif; font-size: 17px; color: var(--orange); letter-spacing: 0.5px;
  }

  /* front side */
  .card-front { left: 600px; top: 440px; background: var(--paper); }
  .card-front .halo { position: absolute; right: -20px; top: 26px; width: 170px; height: 170px; border-radius: 50%; background: var(--peach); }
  .card-front .brand { position: absolute; left: 36px; top: 30px; display: flex; align-items: center; gap: 16px; }
  .card-front .brand-dot { width: 56px; height: 56px; border-radius: 50%; background: var(--orange); }
  .card-front .brand-name {
    font-family: "Open Sans", sans-serif; font-weight: 400; font-size: 54px;
    color: var(--ink); line-height: 1;
  }
  .card-front .accent-bar { position: absolute; left: 0; top: 128px; width: 9px; height: 40px; background: var(--orange); }
  .card-front .person { position: absolute; left: 36px; top: 128px; font-family: "Arimo", sans-serif; }
  .card-front .person-name { font-weight: 700; font-size: 22px; color: var(--orange); }
  .card-front .person-role { font-size: 16px; color: var(--ink-soft); margin-top: 2px; }

  .card-front .contact {
    position: absolute; right: 28px; bottom: 20px;
    font-family: "Arimo", sans-serif; font-size: 17px; line-height: 21px;
    color: var(--ink-soft); text-align: right; list-style: none;
  }
  .card-front .contact li { display: flex; justify-content: flex-end; align-items: center; gap: 10px; }
  .card-front .contact .plain { padding-right: 24px; }
  .card-front .contact svg { width: 14px; height: 14px; flex: none; }
</style>
</head>
<body>
<main class="stage">

  <section class="card card-back" aria-label="Card back">
    <div class="brand">
      <span class="brand-dot"></span>
      <span class="brand-name">velmora</span>
    </div>
    <p class="tagline">Assessment, simplified</p>
  </section>

  <section class="card card-front" aria-label="Card front">
    <span class="halo"></span>
    <div class="brand">
      <span class="brand-dot"></span>
      <span class="brand-name">velmora</span>
    </div>
    <span class="accent-bar"></span>
    <div class="person">
      <p class="person-name">Joe Smith</p>
      <p class="person-role">General Manager</p>
    </div>
    <ul class="contact">
      <li class="plain">Streetname</li>
      <li class="plain">Cityname Suburbname</li>
      <li class="plain">London - UK</li>
      <li>+00 1234 5678
        <svg viewBox="0 0 14 14" aria-hidden="true"><path d="M3 1 L5.5 3.5 L4.2 5.2 Q5.5 8 8.8 9.8 L10.5 8.5 L13 11 L11 13 Q5 12 1 3 Z" fill="var(--orange)"/></svg>
      </li>
      <li>mail@email.com
        <svg viewBox="0 0 14 14" aria-hidden="true"><rect x="1" y="3" width="12" height="8" rx="1" fill="var(--orange)"/><path d="M1.5 3.5 L7 8 L12.5 3.5" fill="none" stroke="#fff" stroke-width="1.2"/></svg>
      </li>
      <li>www.website.com
        <svg viewBox="0 0 14 14" aria-hidden="true"><circle cx="7" cy="7" r="6" fill="var(--orange)"/><ellipse cx="7" cy="7" rx="2.5" ry="6" fill="none" stroke="#fff" stroke-width="1"/><line x1="1" y1="7" x2="13" y2="7" stroke="#fff" stroke-width="1"/></svg>
      </li>
    </ul>
  </section>

</main>
</body>
</html>
```